Business Card Design and Logo Needed

I need Business Cards and a Logo for my website and public speaking business which can be found at: www.kelsa-thorn.example

I'm looking for creative and unique ideas. Some business cards I've found online that I like can be found at:
http://gigplatelo.example/general/18-smokin-hot-business-card-designs/

and at

http://www.vortaplume.example/2009/04/50-creative-business-cards-of-50-graphic-designers/

```html
<!DOCTYPE html>
<html lang="en">
<head>
<meta charset="utf-8">
<title>Kelsa Thorn – Business Card</title>
<link rel="stylesheet" href="https://fonts.googleapis.com/css2?family=Marcellus&family=Source+Sans+3:wght@400;600&display=swap">
<style>
  :root {
    --backdrop: #dcdcdc;
    --card: #f4dfb6;
    --card-light: #f8e8c6;
    --band: #260805;
    --ink: #3a1a12;
    --diamond-deep: #3e110e;
    --diamond-mid: #5e1d18;
    --name-ink: #f1dab0;
    --rule: #6b4a3a;
  }
  * { box-sizing: border-box; margin: 0; padding: 0; }
  html, body {
    width: 1200px;
    height: 895px;
    overflow: hidden;
    background: var(--backdrop);
  }
  .card {
    position: absolute;
    left: 251px;
    top: 238px;
    width: 698px;
    height: 419px;
    border-radius: 30px;
    overflow: hidden;
    background: radial-gradient(ellipse at 40% 40%, var(--card-light), var(--card) 70%);
    font-family: "Source Sans 3", "Myriad Pro", sans-serif;
    color: var(--ink);
  }
  .tagline {
    position: absolute;
    left: 55px;
    top: 150px;
    font-size: 13px;
    font-weight: 600;
    letter-spacing: 0.1px;
  }
  .emblem {
    position: absolute;
    left: 417px;
    top: 31px;
    width: 258px;
    height: 256px;
  }
  .emblem svg { position: absolute; inset: 0; }
  .name {
    position: absolute;
    left: 0;
    right: 0;
    top: 108px;
    text-align: center;
    font-family: "Marcellus", "Trajan Pro", serif;
    font-size: 22px;
    letter-spacing: 0.5px;
    color: var(--name-ink);
  }
  .job-title {
    position: absolute;
    left: 146px;
    top: 135px;
    font-family: "Marcellus", "Trajan Pro", serif;
    font-size: 12px;
    letter-spacing: 0.3px;
    color: var(--name-ink);
  }
  .contacts {
    position: absolute;
    left: 0;
    top: 321px;
    width: 100%;
    height: 55px;
  }
  .contact {
    position: absolute;
    display: flex;
    align-items: center;
    font-size: 13.5px;
    font-weight: 600;
    height: 20px;
  }
  .contact svg { width: 13px; height: 13px; fill: var(--ink); }
  .contact .icon { position: absolute; width: 13px; }
  .contact .value { position: absolute; white-space: nowrap; }
  .divider {
    position: absolute;
    top: 0;
    width: 1px;
    height: 55px;
    background: var(--rule);
  }
  .band {
    position: absolute;
    left: 0;
    bottom: 0;
    width: 100%;
    height: 43px;
    background: var(--band);
  }
</style>
</head>
<body>
  <div class="card">
    <p class="tagline">Speaker, Philanthropist, and Author of Forthcoming Book</p>

    <div class="emblem">
      <svg viewBox="0 0 258 256" role="img" aria-label="Diamond panel with dark red floral damask pattern framed by curled-back paper edges">
        <defs>
          <linearGradient id="curl" x1="0" y1="0" x2="1" y2="1">
            <stop offset="0" stop-color="#f2dcb0"/>
            <stop offset="1" stop-color="#c9a979"/>
          </linearGradient>
          <radialGradient id="damask" cx="0.5" cy="0.5" r="0.6">
            <stop offset="0" stop-color="#5e1d18"/>
            <stop offset="1" stop-color="#3e110e"/>
          </radialGradient>
        </defs>
        <polygon points="129,8 250,128 129,248 8,128" fill="url(#curl)" opacity="0.9"/>
        <polygon points="129,0 258,128 129,256 0,128" fill="url(#damask)"/>
      </svg>
      <div class="name">KELSA THORN</div>
      <div class="job-title">JOB TITLE</div>
    </div>

    <div class="contacts">
      <div class="divider" style="left:111px"></div>
      <div class="divider" style="left:290px"></div>

      <div class="contact" style="left:0; top:0">
        <span class="icon" style="left:88px">
          <svg viewBox="0 0 16 16"><path d="M2 6c0-2 2-3 6-3s6 1 6 3v1h-3V5.5H5V7H2z"/><path d="M4 8h8l2 5H2z"/></svg>
        </span>
        <span class="value" style="left:124px">00 123.4567.890</span>
      </div>
      <div class="contact" style="left:0; top:31px">
        <span class="icon" style="left:88px">
          <svg viewBox="0 0 16 16"><rect x="2" y="5" width="12" height="10" rx="1"/><rect x="4" y="1" width="8" height="4" fill="none" stroke="#3a1a12" stroke-width="1.5"/><rect x="4" y="7" width="8" height="1.5" fill="#f4dfb6"/><rect x="4" y="10" width="2" height="2" fill="#f4dfb6"/><rect x="7" y="10" width="2" height="2" fill="#f4dfb6"/><rect x="10" y="10" width="2" height="2" fill="#f4dfb6"/></svg>
        </span>
        <span class="value" style="left:124px">00 123.4567.890</span>
      </div>
      <div class="contact" style="left:0; top:0">
        <span class="icon" style="left:275px">
          <svg viewBox="0 0 16 16"><rect x="4" y="1" width="8" height="5"/><rect x="2" y="6" width="12" height="8" rx="1"/><rect x="4" y="9" width="8" height="1.5" fill="#f4dfb6"/></svg>
        </span>
        <span class="value" style="left:305px">00 123.4567.890</span>
      </div>
      <div class="contact" style="left:0; top:31px">
        <span class="icon" style="left:275px">
          <svg viewBox="0 0 16 16"><rect x="1" y="4" width="14" height="9"/><path d="M1 4l7 5 7-5" fill="none" stroke="#f4dfb6" stroke-width="1.3"/></svg>
        </span>
        <span class="value" style="left:305px; font-size:13px">Kelsathorn@kelsa-thorn.example</span>
      </div>
    </div>

    <div class="band"></div>
  </div>
</body>
</html>
```